Essential Oils and Chemical Free Skincare Packaging

We have a range of 100% organic 10ml essential oils and 10ml essential oil synergy blends and 50ml spritzer bottles plus chemical free skincare products including two serums, one cleanser, two moisturisers, a lip balm, an eye and lip cream and a body lotion that need new labels, boxes for the products with a fresh new look. Some of these products are in packs or gift packs as seen on the website. Our logo is attached, we love the logo colours. Our website is www.olbrena.com. We have high quality, chemical-free and organic ingredients and amazingly effective products. The packaging now needs to reflect the contents and the prices of the precious ingredients. We think we would like to stick to the amber glass, thinking of black lids. Want it to feel professional, classy, high-end, classic and not fussy. Would love for the packaging to feel fresh, beautiful, natural, expensive... yet still affordable luxury. New packaging could be predominantly grey and white with flash of the green. Our customer is busy and health conscious. She does not need a lot of fuss but loves using beautiful products. Some of our tag lines include - 'Beauty is being yourself but with a sparkle.' and 'Self-care is your divine responsibility.' Olbrena wakes your body, your spirit and your heart.' Can you please look at the product jars and bottles as well as the boxes that the oils will be packaged in.

Target Market(s)

30-50yr females, business women, entrepreneurs, health conscious mum's all with an awareness around the importance of chemical-free and organic products and a love for health, fitness and real beauty.

Colors

Requirements
Must have
• Our logo and our logo colours incorporated. As mentioned could be predominantly silver/grey and white with splash of green. The bottles could even be printed in the one silver/grey colour directly onto the glass as an option. Or labels to wrap around the bottles. Boxes (which are separate to the bottles) containing the products to be inviting and speak luxury. Must be recyclable in alignment with our values.
Nice to have
• Not sure whether to look at printing on the glass direct or complete wrap around labels (which will no doubt be cheaper to create). Would love a number of design options and ideas that give that beautiful feel and would make our customer so excited to want these products. Our packaging is over 8 years old and we have grown significantly in this time. It would be nice to have a new fresh look that reflects the quality and amazing efficacy of these products.
• One suggestion regarding the packaging for the essential oils is to categorise them - so the floral oils like lavender, geranium, neroli and rose all have a certain colour or something on the packaging to distinguish them as floral oils. Then we have herbal, spicy, woody, grass and citrus categories too. This could be shown on the box as opposed to the bottle.
• We also have four kinds of synergy blends that are based on the four main personality types eg: Powerful, Playful, Peaceful and Precise. No one necessarily knows this unless I am speaking but the oil blends that fit in here are Powerful - Cleanse & Fortify, Shield Lift and Valour & Boldness. Playful - Passion & Closeness, Rejoice & Brighten and Zest & Heat. Peaceful - Quick Hush, Stillness & Prayer and Unwind & Renew. Precise - Poise & Accord, Spark & Liveliness and Aim & Lucidity.
• I also love to incorporate the four seasons and we have four one-off seasonal blends called Cradle Us (winter), Kindle Us (spring), Hold Us (summer) and Anchor Us (autumn).
• If there was a strong element of natural beauty with this new packaging that would be amazing.
Should not have
• Lots of different wild out there colours. We love nature, and plants and order and clarity. Should not have too much information or busyness. Needs to be simple, elegant, classy, classic, beautiful. Please do not go cottage/lavender farm industry looking.

```html
<!DOCTYPE html>
<html lang="en">
<head>
<meta charset="utf-8">
<title>Olbrena – Chamomile Roman Oil Label</title>
<link href="https://fonts.googleapis.com/css2?family=Questrial&family=Roboto+Condensed:wght@300&display=swap" rel="stylesheet">
<style>
  :root {
    --canvas-bg: #f3f3f1;
    --label-green: #b4e854;
    --label-white: #ffffff;
    --ink: #1b1b1b;
    --ink-soft: #3a3a3a;
    --rule-green: #cfe9a0;
    --label-edge: #cfd2cc;
    --art-light: #f4f6ef;
    --art-green: #c9dcae;
  }
  * { margin: 0; padding: 0; box-sizing: border-box; }
  html, body {
    width: 1200px;
    height: 849px;
    overflow: hidden;
    background: var(--canvas-bg);
  }
  .label {
    position: absolute;
    left: 100px;
    top: 170px;
    width: 1000px;
    height: 508px;
    display: flex;
    border: 1px solid var(--label-edge);
    box-shadow: 0 4px 10px rgba(0,0,0,0.08);
  }
  .info-block {
    width: 566px;
    height: 100%;
    background: var(--label-green);
    display: flex;
  }
  .info-copy {
    width: 440px;
    padding: 16px 10px 0 24px;
    font-family: "Roboto Condensed", "Arial Narrow", sans-serif;
    font-weight: 300;
    font-size: 24px;
    line-height: 43px;
    color: var(--ink);
    letter-spacing: -0.3px;
  }
  .brand-column {
    flex: 1;
    position: relative;
  }
  .brand-name {
    position: absolute;
    left: 50%;
    top: 50%;
    transform: translate(-50%, -50%) rotate(-90deg);
    display: flex;
    align-items: center;
    gap: 18px;
    font-family: "Questrial", sans-serif;
    font-weight: 400;
    font-size: 54px;
    letter-spacing: 6px;
    color: var(--ink);
    white-space: nowrap;
  }
  .brand-dot {
    width: 14px;
    height: 14px;
    border-radius: 50%;
    background: var(--ink);
  }
  .product-block {
    flex: 1;
    background: var(--label-white);
    padding: 10px 12px 0 8px;
    font-family: "Questrial", sans-serif;
    color: var(--ink);
    display: flex;
    flex-direction: column;
  }
  .product-title {
    font-size: 70px;
    font-weight: 400;
    line-height: 84px;
    letter-spacing: 0.5px;
  }
  .title-line { display: flex; justify-content: space-between; }
  .product-specs {
    margin-top: 14px;
    font-size: 26px;
    line-height: 44px;
    color: var(--ink-soft);
  }
  .product-specs p { border-bottom: 1px solid var(--rule-green); }
  .product-illustration {
    margin-top: 20px;
    margin-left: 14px;
    width: 230px;
    height: 140px;
    background: linear-gradient(120deg, var(--art-light) 30%, var(--art-green) 100%);
  }
</style>
</head>
<body>
  <main class="label">
    <section class="info-block">
      <div class="info-copy">
        Lorem ipsum dolor sit amet, consectetur adipiscing elit, sed do eiusmod tempor incididunt ut labore et dolore magna aliqua. Ut enim ad minim veniam, quis nostrud exercitation ullamco laboris nisi ut aliquip ex ea commodo consequat. Duis aute irure dolor in reprehenderit in voluptate velit esse cillum dolore eu fugiat nulla pariatur. Excepteur sint occaecat cupidatat non proident, sunt in culpa qui officia deserunt mollit anim id est laborum.
      </div>
      <div class="brand-column">
        <div class="brand-name"><span class="brand-dot"></span>OLBRENA</div>
      </div>
    </section>
    <section class="product-block">
      <h1 class="product-title">
        <span class="title-line">CHAMOMILE</span>
        <span class="title-line"><span>ROMAN</span><span>OIL</span></span>
      </h1>
      <div class="product-specs">
        <p>Arthemis nobilis</p>
        <p>100% Pure Organic Essencial Oil</p>
        <p>10ml/0.34 fl.oz e</p>
      </div>
      <div class="product-illustration" role="img" aria-label="Illustration of a chamomile flower with green leaves"></div>
    </section>
  </main>
</body>
</html>
```